I am a Vantrell Service and Marketing Consultant looking for a Vantrellesque but business like cover wit

I need a bookcover designed for my new business book titled; "Orderly Wonder. 7 Bright Doors To Vantrellize Your Firm. Outshine, Outlast & Outgrow Your Rivals in EVERY Climate"

The name of my company is Harbor Care Today

We work with companies to implement Vantrell Style Service and Themeing, and then create marketing campaigns to promote that level of service.

I have used Owl Whisper font in the past, but am not tied to it

Target Market(s)

Small Business owners, medical practices, law firms

Industry/Entity Type

Business

Requirements
Must have
• Colors: RGB 30, 54, 128 AND 113, 191, 76. These are the two colors in my logo, if you need it.
Nice to have
• Magic Key?? Gloved Hand (similar to a Vantrell Character)??
Should not have
• Any copyright protected inages

```html
<!DOCTYPE html>
<html lang="en">
<head>
<meta charset="utf-8">
<title>Orderly Wonder – Book Cover</title>
<link rel="stylesheet" href="https://fonts.googleapis.com/css2?family=Oswald:wght@500;700&display=swap">
<style>
  :root {
    --navy: rgb(30, 54, 128);
    --green: rgb(113, 191, 76);
    --paper: #ffffff;
    --backdrop: #f2f2f2;
    --gold-light: #e8c46a;
    --gold-mid: #c8953a;
    --gold-dark: #8a5e1e;
  }
  * { box-sizing: border-box; margin: 0; padding: 0; }
  html, body {
    width: 930px;
    height: 1200px;
    overflow: hidden;
    background: var(--backdrop);
  }
  .canvas {
    position: relative;
    width: 930px;
    height: 1200px;
  }
  .cover {
    position: absolute;
    left: 145px;
    top: 120px;
    width: 640px;
    height: 960px;
    background: var(--paper);
    box-shadow: 0 10px 30px rgba(0,0,0,0.18);
    overflow: hidden;
    font-family: "Oswald", "Arial Narrow", sans-serif;
    color: var(--navy);
  }
  .title-band {
    height: 360px;
    background: var(--green);
    display: flex;
    flex-direction: column;
    align-items: center;
    justify-content: center;
    padding: 0 24px;
  }
  .title {
    text-transform: uppercase;
    font-weight: 700;
    line-height: 0.95;
    text-align: center;
  }
  .title .line-one {
    display: block;
    font-size: 92px;
    letter-spacing: 2px;
  }
  .title .line-two {
    display: block;
    font-size: 142px;
    letter-spacing: 2px;
  }
  .subtitle {
    display: flex;
    align-items: center;
    justify-content: center;
    gap: 18px;
    margin-top: 34px;
    text-transform: uppercase;
    font-weight: 700;
  }
  .subtitle .number {
    font-size: 170px;
    line-height: 0.85;
  }
  .subtitle .words {
    font-size: 42px;
    line-height: 1.05;
    text-align: right;
  }
  .key-art {
    display: block;
    margin: 24px auto 0;
    width: 560px;
    height: 150px;
    border-radius: 75px 30px 30px 75px;
    background: linear-gradient(180deg, var(--gold-light) 0%, var(--gold-mid) 55%, var(--gold-dark) 100%);
  }
  .imprint {
    display: flex;
    align-items: center;
    justify-content: center;
    gap: 8px;
    margin-top: 14px;
    font-size: 16px;
    font-weight: 500;
    color: var(--green);
  }
  .imprint .mark {
    width: 14px;
    height: 14px;
    border-radius: 50%;
    background: var(--navy);
  }
  .tagline {
    margin-top: 12px;
    text-align: center;
    text-transform: uppercase;
    font-weight: 700;
    font-size: 27px;
    line-height: 1.15;
  }
  .author {
    margin-top: 14px;
    text-align: center;
    text-transform: uppercase;
    font-weight: 700;
    font-size: 34px;
    letter-spacing: 1px;
  }
</style>
</head>
<body>
<div class="canvas">
  <article class="cover">
    <header class="title-band">
      <h1 class="title">
        <span class="line-one">Orderly</span>
        <span class="line-two">Wonder</span>
      </h1>
    </header>

    <h2 class="subtitle">
      <span class="number">7</span>
      <span class="words">Bright Doors<br>To Vantrellize<br>Your Firm</span>
    </h2>

    <div class="key-art" role="img" aria-label="Ornate antique gold key lying horizontally"></div>

    <div class="imprint">
      <span class="mark"></span>
      <span class="imprint-name">Harbor Care Today</span>
    </div>

    <p class="tagline">Outshine, Outlast &amp;<br>Outgrow Your Rivals in Every Climate</p>

    <p class="author">Author Name</p>
  </article>
</div>
</body>
</html>
```